Lullwick Aromatherapy Sleep Mask

We need package design for a new product we're introducing that allows for the integration of a variety of aromatherapy blends into a sleep mask. The blends are applied to scent wafers that are embedded inside the mask. The packaging should allow for incorporation of the mask, a .75ml vial of aromatherapy (2-⅛" tall and ⅞" in diameter), a small pipette(2-¼" in length) and five scent wafers (each ¾" in diameter) -- see attached pics. I'd also like to find a way to incorporate a small brochure inside the packaging to explain how to use the product and its benefits.

Target Market(s)

Target is cross gender. The majority of these masks will be used to enhance sleep and insomnia knows no gender preference. Demographic skew is likely college educated, upscale with HHI of $100K+.

Industry/Entity Type

Product

Font styles to use
Serif
Sans Serif

Requirements
Must have
• The ability to incorporate all components: mask, aromatherapy vial, pipette and scent wafers. While I'm happy to review all designs, I need to make sure that the actual production remains affordable so please keep that in mind. Color palette must work with the logo (attached) and be soothing in nature.
Nice to have
• I'd like to see a box option where all components can be securely packaged. I also think it would be nice if the customer can see the actual mask as they will come in a variety of fabrics. Am open to any other suggestions you all have.

```html
<!DOCTYPE html>
<html lang="en">
<head>
<meta charset="utf-8">
<title>Lullwick Aromatherapy Sleep Mask – Box Front</title>
<link rel="stylesheet" href="https://fonts.googleapis.com/css2?family=Questrial&display=swap">
<style>
  :root {
    --stage: #1d1d1f;
    --panel-top: #ffffff;
    --panel-bottom: #e6f4f1;
    --teal: #5eb3a9;
    --teal-light: #a9dcd4;
    --teal-deep: #3f958b;
    --ink: #6b7472;
    --ink-soft: #8a9391;
    --window-edge: #7cc3b9;
  }
  * { margin: 0; padding: 0; box-sizing: border-box; }
  html, body {
    width: 1200px;
    height: 1000px;
    overflow: hidden;
    background: var(--stage);
    font-family: "Questrial", "Century Gothic", sans-serif;
  }
  .box-front {
    position: absolute;
    left: 316px;
    top: 327px;
    width: 568px;
    height: 346px;
    background: linear-gradient(180deg, var(--panel-top) 0%, var(--panel-top) 55%, var(--panel-bottom) 100%);
    overflow: hidden;
  }
  .box-front__art {
    position: absolute;
    inset: 0;
  }
  .component-window {
    position: absolute;
    left: 28px;
    top: 30px;
    width: 134px;
    height: 290px;
    border: 2px solid var(--window-edge);
    background: #dff0ec;
    box-shadow: inset 0 0 0 4px #cfe9e4;
  }
  .component-window__vial {
    position: absolute;
    left: 6px; top: 6px; right: 6px;
    height: 200px;
    background: linear-gradient(90deg, #d9d4c8 0%, #d9d4c8 18%, #2b2f2e 30%, #3a3f3d 60%, #f4f6f5 62%, #f4f6f5 88%, #2b2f2e 92%);
  }
  .component-window__wafers {
    position: absolute;
    left: 6px; right: 6px; bottom: 6px;
    height: 68px;
    background: linear-gradient(180deg, #f4f6f6 0%, #d7dddc 100%);
  }
  .brand-name {
    position: absolute;
    left: 260px;
    top: 186px;
    font-size: 46px;
    letter-spacing: 4px;
    color: var(--teal);
    line-height: 1;
  }
  .brand-dot {
    position: absolute;
    left: 212px;
    top: 192px;
    width: 34px;
    height: 34px;
    border-radius: 50%;
    background: var(--teal-light);
  }
  .contents {
    position: absolute;
    left: 200px;
    top: 254px;
    color: var(--ink);
  }
  .contents__label {
    font-size: 12.5px;
    letter-spacing: 1px;
    color: var(--ink-soft);
    margin-bottom: 3px;
  }
  .contents__list {
    list-style: none;
    display: grid;
    grid-template-columns: 222px 160px;
    row-gap: 3px;
  }
  .contents__item {
    position: relative;
    padding-left: 16px;
    font-size: 12.5px;
    letter-spacing: 1px;
    color: var(--ink-soft);
    line-height: 16px;
  }
  .contents__item::before {
    content: "";
    position: absolute;
    left: 2px;
    top: 5px;
    width: 7px;
    height: 7px;
    background: var(--teal-light);
  }
  .contents__item--lead {
    font-size: 15px;
    color: var(--ink);
    letter-spacing: 0.8px;
  }
</style>
</head>
<body>
  <main class="box-front">
    <svg class="box-front__art" width="568" height="346" viewBox="0 0 568 346">
      <defs>
        <linearGradient id="mask-fabric" x1="0" y1="0" x2="1" y2="0">
          <stop offset="0" stop-color="#2a2f86"/>
          <stop offset="0.35" stop-color="#1f6fa8"/>
          <stop offset="0.6" stop-color="#a9a640"/>
          <stop offset="0.8" stop-color="#7a2f86"/>
          <stop offset="1" stop-color="#2a4f9a"/>
        </linearGradient>
      </defs>
      <rect class="mask-window" x="197" y="35" width="377" height="140" fill="url(#mask-fabric)" role="img" aria-label="Patterned fabric of the sleep mask seen through the window"/>
      <path class="wave-panel" d="M190,30 C250,50 300,150 410,150 C480,150 540,138 574,128 L574,346 L190,346 Z" fill="#ffffff"/>
      <path class="wave-band" d="M190,30 C250,50 300,150 410,150 C480,150 540,138 574,128" fill="none" stroke="var(--teal)" stroke-width="7"/>
      <path class="wave-band-light" d="M200,44 C258,66 304,160 410,160 C480,160 540,148 574,140" fill="none" stroke="var(--teal-light)" stroke-width="4"/>
    </svg>

    <div class="component-window">
      <div class="component-window__vial" role="img" aria-label="Aromatherapy vial and pipette in their tray"></div>
      <div class="component-window__wafers" role="img" aria-label="Five round scent wafers"></div>
    </div>

    <span class="brand-dot"></span>
    <h1 class="brand-name">lullwick</h1>

    <section class="contents">
      <p class="contents__label">includes:</p>
      <ul class="contents__list">
        <li class="contents__item contents__item--lead">Sleeping Mask</li>
        <li class="contents__item">Small pipette</li>
        <li class="contents__item">75ml vial of aromatherapy</li>
        <li class="contents__item">Five scent wafers</li>
      </ul>
    </section>
  </main>
</body>
</html>
```